Home change of address

Martin & Priya Colwell
WE HAVE MOVED
The address of our new home is
Birch Hollow
47 Thornbury Lane Road
Ashcombe on Wend
Warwickshire
B72 8QT
Tel: 07912 384071
Email: martin@pelmora.uk.com

```html
<!DOCTYPE html>
<html lang="en">
<head>
<meta charset="utf-8">
<title>We Have a New Home – Martin &amp; Priya Colwell</title>
<link rel="stylesheet" href="https://fonts.googleapis.com/css2?family=Crimson+Text:wght@400;600&family=Playfair+Display:wght@800&display=swap">
<style>
  :root {
    --paper: #ffffff;
    --ink: #262f38;
    --slate-leaf: #3f5866;
    --olive-bark: #7a6410;
    --rock: #c9c9c9;
    --fern: #2f8a5e;
  }
  * { margin: 0; padding: 0; box-sizing: border-box; }
  html, body { width: 1200px; height: 851px; overflow: hidden; background: var(--paper); }
  .card {
    position: relative;
    width: 1200px;
    height: 851px;
    background: var(--paper);
    color: var(--ink);
    font-family: "Crimson Text", Georgia, serif;
    overflow: hidden;
  }
  .corner-leaf {
    position: absolute;
    left: -14px;
    top: 28px;
    width: 24px;
    height: 98px;
    border-radius: 50%;
    background: linear-gradient(180deg, #4fb07f, var(--fern));
  }
  .olive-grove {
    position: absolute;
    left: -40px;
    top: 396px;
    width: 414px;
    height: 470px;
    border-radius: 48% 52% 10% 10% / 42% 42% 8% 8%;
    background:
      radial-gradient(ellipse 60% 42% at 55% 32%, var(--slate-leaf) 0%, rgba(63,88,102,0.55) 60%, rgba(63,88,102,0) 100%),
      linear-gradient(180deg, rgba(255,255,255,0) 45%, rgba(122,100,16,0.75) 70%, var(--rock) 100%);
  }
  .headline {
    position: absolute;
    left: 0; top: 0;
    width: 100%;
    height: 230px;
  }
  .headline__lead {
    position: absolute;
    left: 118px;
    top: 152px;
    font-size: 49px;
    line-height: 1;
    letter-spacing: 0.12em;
    font-weight: 400;
    white-space: nowrap;
  }
  .headline__word {
    position: absolute;
    top: 60px;
    font-family: "Playfair Display", Georgia, serif;
    font-weight: 800;
    font-size: 150px;
    line-height: 1;
    color: var(--ink);
  }
  .headline__word--h { left: 578px; }
  .headline__word--m { left: 806px; }
  .headline__word--e { left: 976px; }
  .headline__o {
    position: absolute;
    left: 694px;
    top: 116px;
    width: 88px;
    height: 88px;
    border-radius: 50%;
    border: 1px solid var(--ink);
    background: radial-gradient(circle at 50% 40%, var(--slate-leaf) 0%, #6d7f6a 45%, var(--olive-bark) 100%);
  }
  .details {
    position: absolute;
    right: 128px;
    top: 300px;
    text-align: right;
    font-size: 34px;
    letter-spacing: 0.12em;
    line-height: 72px;
    white-space: nowrap;
  }
  .contact {
    position: absolute;
    top: 772px;
    font-size: 29px;
    letter-spacing: 0.12em;
    white-space: nowrap;
  }
  .contact--tel { left: 260px; }
  .contact--email { left: 614px; }
</style>
</head>
<body>
  <main class="card">
    <div class="corner-leaf" role="img" aria-label="Green leaf illustration at the top-left edge"></div>
    <div class="olive-grove" role="img" aria-label="Illustration of a large olive tree with two small olive trees and grey rocks"></div>

    <h1 class="headline">
      <span class="headline__lead">WE HAVE A NEW</span>
      <span class="headline__word headline__word--h">h</span>
      <span class="headline__o" role="img" aria-label="Letter o drawn as a circle containing a small olive tree illustration"></span>
      <span class="headline__word headline__word--m">m</span>
      <span class="headline__word headline__word--e">e</span>
    </h1>

    <address class="details" style="font-style: normal;">
      <p class="details__names">Martin &amp; Priya Colwell</p>
      <p class="details__street">Birch Hollow,47 Thornbury Lane Road,</p>
      <p class="details__town">Ashcombe on Wend,Warwickshire, B72 8QT.</p>
    </address>

    <p class="contact contact--tel">Tel: 07912 384071</p>
    <p class="contact contact--email">Email: martin@pelmora.uk.com</p>
  </main>
</body>
</html>
```